New Toothpaste brand needs a logo & packaging design

Our company is launching a new toothpaste and is looking for a logo and packaging design. The toothpaste brand is called Brivana. The packaging should have the same design quality as the major international brands, such as Lumora, Lumora Totalcare, Dentiva, Pexolo, Wind-rise, Marvest, etc. The dominant colors for our brand should be hues of blue, similar to other major brands. In addition, there should be a little bit of green to represent the "Fresh Mint Blast" flavor and the "Extracts of Aloe Vera" included in the ingredients.

There are typically 3 unique sides on a toothpaste box:

The face: Repeated on ~3 sides of the 4 faces of the box
The back: The 4th box face has the instructions for use, ingredients, company information, bar code/product info, and some branding elements.
The sides: Usually consisting of just the logo, flavor etc.

Please refer to existing brands such as Lumora, Lumora Total-care, and Dentiva for an example of typical box layout and elements.

Task Details:
Package Dimensions: 180 mm x 48 mm x 28 mm, 100 ml toothpaste tube
Brand Name: Brivana
Description: Fluoride Toothpaste
Flavor: Fresh Mint Blast
5 Actions: Protects against cavities and tartar, freshens breath, whitens teeth, and maintains healthy gums. These actions can also be made into a list like Lumora Total Care or Dentiva Max care. For instance, Strong Teeth, Fresh Breath, Whitening, Healthy Gums, Cavity and Tartar Protection.
Also contains whitening micro particles and extracts of aloe vera which may be highlighted on the package

Overall, the look should be high quality and with the same look and feel as the big brands mentioned previously. We do not have an existing logo for this brand. The face of the package is the most important element as it is often repeated on several sides and on the tube itself.

Please let me know if you have any questions.

I've attached some of our favorite big brand designs below. I would say the Lumora Total Care and Gleam vers

The logos I've seen so far for Brivana, have been a bit too bold. A little bold is okay, but just needs to be moderate. 

I would like the colors to be bright and appealing. I mentioned shades of blue being the major color, but green should also be highlighted as well, perhaps in a 80% blue to 20% green ratio. 

Target Market(s)

adult consumer of toothpaste, both female and male.

Industry/Entity Type

It Company

Requirements
Must have
• A logo with the brand name: Brivana
Description or sub text: Fluoride Toothpaste
Flavor: Fresh Mint Blast
A phrase or list describing the Toothpaste Actions: e.g., Protects against cavities and tartar, freshens breath, whitens teeth, and maintains healthy gums. Or as a list simialr to Lumora Total Care or Dentiva Max Care:
-Anti-cavity
-Anti-tartar
-Fresh breath
-Whitening
-Healthy Gums

Special ingredient of "whitening micro particles: and "extracts of aloe vera", which should also be highlighted.

The color should mostly be shades of blue, with only a little bit of green to accentuate the fresh mint blast flavor and aloe vera

Nice to have
• The design should really look good next to lumora total care, gleam pure, and dentiva max care. These are our favorite designs.
Should not have
• For aloe vera, there is no need to show the plant.

The Brivana logo shouldn't be too Bold. This should be appeal to all consumers, not just men.

```html
<!DOCTYPE html>
<html lang="en">
<head>
<meta charset="utf-8">
<title>Brivana Toothpaste Box Face</title>
<link href="https://fonts.googleapis.com/css2?family=Montserrat:wght@300;500;600;700&display=swap" rel="stylesheet">
<style>
  :root {
    --page-bg: #ffffff;
    --top-rule: #33358a;
    --blue-deep: #2b46a6;
    --blue-mid: #2463be;
    --blue-bright: #1f86d2;
    --blue-panel: #2f3a98;
    --blue-base: #2950ae;
    --green: #2eb57c;
    --green-light: #43c99a;
    --white: #ffffff;
    --seal-light: #f4f7fc;
    --seal-shade: #aebfdc;
  }
  * { box-sizing: border-box; margin: 0; padding: 0; }
  html, body { width: 1200px; height: 1000px; overflow: hidden; }
  body {
    position: relative;
    background: var(--page-bg);
    font-family: "Montserrat", Arial, sans-serif;
    color: var(--white);
  }
  .top-rule {
    position: absolute; left: 0; top: 0; width: 1200px; height: 8px;
    background: var(--top-rule);
  }
  .box-face {
    position: absolute; left: 206px; width: 789px; height: 187px;
    overflow: hidden;
  }
  .box-face--first { top: 257px; }
  .box-face--second { top: 508px; }

  .front {
    position: absolute; left: 0; top: 0; width: 521px; height: 187px;
    background: linear-gradient(100deg, var(--blue-deep) 0%, var(--blue-mid) 45%, var(--blue-bright) 100%);
  }
  .front__base {
    position: absolute; left: 0; bottom: 0; width: 521px; height: 26px;
    background: linear-gradient(90deg, var(--blue-deep), var(--blue-base));
  }
  .brand-name {
    position: absolute; left: 24px; top: 38px;
    font-size: 70px; font-weight: 600; letter-spacing: -1px; line-height: 1;
    color: var(--white);
  }
  .box-face--second .brand-name { left: 34px; top: 48px; font-size: 74px; }

  .aloe-badge {
    position: absolute; left: 357px; top: 96px; width: 134px; height: 28px;
    background: linear-gradient(90deg, var(--green) 60%, rgba(46,181,124,0.6));
    border-radius: 14px 0 0 14px;
    display: flex; align-items: center;
  }
  .aloe-badge__dot {
    width: 22px; height: 22px; border-radius: 50%;
    background: var(--white); margin-left: 3px; flex: none;
  }
  .aloe-badge__text {
    margin-left: 8px; font-size: 11.5px; font-weight: 700; line-height: 12px;
  }
  .claim-band {
    position: absolute; left: 0; top: 136px; width: 504px; height: 25px;
    background: linear-gradient(90deg, var(--green), var(--green-light));
    font-size: 14px; font-weight: 700; line-height: 25px;
    padding-left: 12px; white-space: nowrap;
  }
  .volume {
    position: absolute; left: 12px; top: 168px;
    font-size: 13px; font-weight: 300;
  }

  .seal-strip {
    position: absolute; left: 521px; top: 0; width: 82px; height: 187px;
    background: var(--blue-bright);
  }
  .seal-strip__drop {
    position: absolute; left: 0; top: 0; width: 82px; height: 167px;
    border-radius: 0 0 41px 41px;
    background: linear-gradient(180deg, var(--white) 0%, #dff3ea 40%, var(--green) 100%);
  }
  .seal-strip__seal {
    position: absolute; left: 11px; top: 89px; width: 60px; height: 60px;
    border-radius: 50%;
    background: radial-gradient(circle at 40% 35%, var(--seal-light), var(--seal-shade));
  }

  .side {
    position: absolute; left: 603px; top: 0; width: 186px; height: 187px;
    background: linear-gradient(180deg, var(--blue-panel), var(--blue-deep));
  }
  .benefit-list {
    position: absolute; left: 42px; top: 17px; list-style: none;
    font-size: 12.5px; font-weight: 700; line-height: 15.6px;
  }
  .flavor-band {
    position: absolute; left: 29px; top: 126px; width: 150px; height: 22px;
    background: linear-gradient(90deg, var(--green), rgba(67,201,154,0.7));
    font-size: 13px; font-weight: 700; line-height: 22px; padding-left: 13px;
    white-space: nowrap;
  }
</style>
</head>
<body>
  <div class="top-rule"></div>

  <section class="box-face box-face--first">
    <div class="front">
      <div class="front__base"></div>
      <div class="brand-name">Brivana</div>
      <div class="aloe-badge"><span class="aloe-badge__dot"></span><span class="aloe-badge__text">EXTRACTS<br>OF ALOE VERA</span></div>
      <div class="claim-band">FLUORIDE TOOTHPASTE WITH WHITENING MICRO PARTICLES</div>
      <div class="volume">100ml</div>
    </div>
    <div class="seal-strip">
      <div class="seal-strip__drop"></div>
      <div class="seal-strip__seal" role="img" aria-label="Dental care seal emblem"></div>
    </div>
    <div class="side">
      <ul class="benefit-list">
        <li>STRONG TEETH</li><li>FRESH BREATH</li><li>WHITENING</li>
        <li>HEALTHY GUMS</li><li>CAVITY</li><li>TARTAR</li>
      </ul>
      <div class="flavor-band">FRESH MINT BLAST</div>
    </div>
  </section>

  <section class="box-face box-face--second">
    <div class="front">
      <div class="front__base"></div>
      <div class="brand-name">Brivana</div>
      <div class="aloe-badge"><span class="aloe-badge__dot"></span><span class="aloe-badge__text">EXTRACTS<br>OF ALOE VERA</span></div>
      <div class="claim-band">FLUORIDE TOOTHPASTE WITH WHITENING MICRO PARTICLES</div>
      <div class="volume">100ml</div>
    </div>
    <div class="seal-strip">
      <div class="seal-strip__drop"></div>
      <div class="seal-strip__seal" role="img" aria-label="Dental care seal emblem"></div>
    </div>
    <div class="side">
      <ul class="benefit-list">
        <li>STRONG TEETH</li><li>FRESH BREATH</li><li>WHITENING</li>
        <li>HEALTHY GUMS</li><li>CAVITY</li><li>TARTAR</li>
      </ul>
      <div class="flavor-band">FRESH MINT BLAST</div>
    </div>
  </section>
</body>
</html>
```